Create Banner Ads for Catholic Business Directory

The orginal web page design project was cancelled and we are looking to use our remaining allocated funds for Banner Ad designs.

We need the designer to create 300x250 and matching 300x125 Banner Ads promoting ParishMarket.com. Please look at website home page with priest (will provide photo). The banner ads will be used on other religious websites to get visitors to click and visit http://ParishMarket.com and find businesses who support Catholic churches.

"Find a Business Supporting Your Church"

Can use other images than those provided. For example religious background or image of church, etc.

Would also like to see a new simple logo graphic for "Parish Trade Locator" included on this project.

Thanks. -walt
Updates

Project Deadline Extended Reason: The original web page design project was cancelled and we are wanting to use our remaining funds for nice Banner Ad designs promoting our website http://parishmarket.com Added Sunday, January 3, 2016

Target Market(s)

Catholics looking for businesses who support the church.

Industry/Entity Type

Religious

Coding

Coded - Design and coding required

Number of Pages Required

1 page

Font styles to use
Serif

Requirements
Must have
• Attractive Clean Appearance.

```html
<!DOCTYPE html>
<html lang="en">
<head>
<meta charset="utf-8">
<title>Parish Trade Locator Banner Ads</title>
<link href="https://fonts.googleapis.com/css2?family=Montserrat:wght@300;400;500;700&family=Arimo:wght@400&display=swap" rel="stylesheet">
<style>
  :root {
    --page-bg: #ffffff;
    --ink: #1a1a1a;
    --brand-blue: #1b3f9c;
    --header-veil: rgba(250, 248, 244, 0.9);
    --headline: #ffffff;
    --field-bg: #ffffff;
    --field-border: #d6d6d6;
    --placeholder: #8a8a8a;
    --cta-red: #ee0a0a;
    --cta-text: #ffffff;
  }
  * { box-sizing: border-box; margin: 0; padding: 0; }
  html, body { width: 1200px; height: 1062px; overflow: hidden; background: var(--page-bg); }
  body { position: relative; font-family: "Montserrat", sans-serif; color: var(--ink); }

  .size-label, .site-url {
    position: absolute; left: 0; width: 1200px; text-align: center;
    font-family: "Montserrat", sans-serif; font-weight: 300; color: var(--ink);
  }
  .size-label { font-size: 30px; letter-spacing: 1px; }
  .size-label--large { top: 100px; left: 9px; }
  .size-label--small { top: 692px; left: 9px; }
  .site-url { top: 1003px; font-size: 29px; letter-spacing: 1.5px; }

  .banner { position: absolute; left: 348px; width: 506px; overflow: hidden; }
  .banner--large { top: 147px; height: 422px; }
  .banner--small { top: 738px; height: 211px; }

  .banner__photo {
    position: absolute; inset: 0;
    background:
      linear-gradient(90deg, rgba(0,0,0,0) 60%, rgba(20,16,14,0.85) 78%, rgba(20,16,14,0.9) 100%),
      radial-gradient(ellipse at 55% 40%, #f1d9a8 0%, #c99456 35%, #6e3e22 70%, #3a1f14 100%);
  }

  .banner__header {
    position: absolute; left: 0; top: 0; width: 100%; height: 67px;
    background: var(--header-veil);
    display: flex; align-items: center;
  }
  .brand { display: flex; align-items: center; margin-left: 16px; }
  .brand__mark { width: 38px; height: 38px; border-radius: 50%; background: var(--brand-blue); flex: none; }
  .brand__name {
    margin-left: 6px; font-weight: 700; font-size: 12.5px; line-height: 14px;
    color: var(--brand-blue); text-transform: uppercase; letter-spacing: 0.2px;
  }
  .nav { display: flex; position: absolute; top: 0; height: 67px; align-items: center; }
  .nav a { color: var(--brand-blue); text-decoration: none; font-weight: 500; font-size: 21px; }
  .banner--large .nav { left: 202px; gap: 29px; }
  .banner--small .nav { left: 164px; gap: 24px; }

  .headline {
    position: absolute; left: 17px; color: var(--headline);
    font-weight: 700; font-size: 30px; line-height: 40px; letter-spacing: -0.3px;
    text-shadow: 0 1px 3px rgba(0,0,0,0.45);
  }
  .banner--large .headline { top: 74px; }
  .banner--small .headline { top: 73px; }

  .field {
    position: absolute; background: var(--field-bg); border: 1px solid var(--field-border);
    border-radius: 3px; font-family: "Arimo", sans-serif; color: var(--placeholder);
    white-space: nowrap; overflow: hidden; display: flex; align-items: center;
  }
  .cta {
    position: absolute; background: var(--cta-red); color: var(--cta-text); border-radius: 3px;
    font-family: "Arimo", sans-serif; display: flex; align-items: center; justify-content: center;
  }

  .banner--large .field { left: 17px; width: 329px; height: 64px; padding-left: 22px; font-size: 23px; }
  .banner--large .field--type { top: 170px; }
  .banner--large .field--location { top: 255px; }
  .banner--large .cta { left: 17px; top: 340px; width: 329px; height: 66px; font-size: 23px; }

  .banner--small .field { top: 154px; height: 49px; padding-left: 20px; font-size: 20px; }
  .banner--small .field--type { left: 3px; width: 161px; }
  .banner--small .field--location { left: 172px; width: 161px; }
  .banner--small .cta { left: 341px; top: 154px; width: 161px; height: 49px; font-size: 20px; }
</style>
</head>
<body>
  <div class="size-label size-label--large">300 X 250</div>

  <section class="banner banner--large">
    <div class="banner__photo" role="img" aria-label="Warm church interior with a smiling priest holding a lectionary on the right"></div>
    <header class="banner__header">
      <div class="brand"><span class="brand__mark"></span><span class="brand__name">Parish<br>Trade<br>Locator</span></div>
      <nav class="nav"><a href="#">Search</a><a href="#">Review</a><a href="#">Connect</a></nav>
    </header>
    <h1 class="headline">Find A Business<br>Supporting Your Church</h1>
    <div class="field field--type">Type of business?</div>
    <div class="field field--location">Search by location...</div>
    <div class="cta">Search Now</div>
  </section>

  <div class="size-label size-label--small">300 X 125</div>

  <section class="banner banner--small">
    <div class="banner__photo" role="img" aria-label="Warm church interior with a priest on the right"></div>
    <header class="banner__header">
      <div class="brand"><span class="brand__mark"></span><span class="brand__name">Parish<br>Trade<br>Locator</span></div>
      <nav class="nav"><a href="#">Search</a><a href="#">Review</a><a href="#">Connect</a></nav>
    </header>
    <h1 class="headline">Find A Business<br>Supporting Your Church</h1>
    <div class="field field--type">Business typ</div>
    <div class="field field--location">City/Post Coc</div>
    <div class="cta">Search Now</div>
  </section>

  <div class="site-url">HTTP://PARISHMARKETCOM.SITEPREVIEW.IO/</div>
</body>
</html>
```